"Lantern Field" Play - Poster Design for Theatre Group

We are an amateur theatre group based in Geneva, Switzerland. We take pride in eye-catching posters for our shows, which are printed in various sizes.
This design will be for a play in March 2016. The play is called "Lantern Field", and it's a Harwick Medal winner from Marcus Ellery-Pound. The play is about a couple who have everything a family could want, until they lose a child in a life-shattering accident that turns their world upside down. The play charts the couple's bittersweet search to find each other and to find comfort.
Most importantly, we want a design that will make people want to see the show. We don't want to give away the plot or be too heavy-handed about death, but we want it to be clear that it's not a comedy (although there are some lighter moments!).
Attached you will find a template for the poster. This simply has our group name and logo in the top right corner: (Lakeshore Stage Players Circle presents).
You may change the color of both the text and the logo, but please do not change the font, size, or location.
Here is the information that needs to be on the poster, wherever you see fit:
play title: Lantern Field
author byline: by Marcus Ellery-Pound
director line: directed by Rob Feltwick
tagline: How do you keep it together when your whole world's fallen apart?
dates and times:
1-5 March 2016
(Tue-Fri 20:00, Sat 19:00)
location:
Théâtre du Vieux-Moulin
Eaux-Vives, Geneva
websites:
www.lspc.ch
www.scenelettres.ch
Technical Details:
Any font or combination of fonts is acceptable. The largest text should be the play title. The author's name must be at least 50% of the title font size.
For this competition, we would like the version with A3 proportions, which will also be used at F4 (89.5 x 128 cm) and A5 sizes (14.8 x 21 cm). Therefore no text should be below 9pt at A5.
However, from the winning designer we will also need repurposed sizes of the same design. Here is a comprehensive list of the sizes we will need.
1) A3 print poster. Artwork should be 300dpi, CMYK, sent with a 1mm bleed all round, to specification PDF/X-1A:2001. We will need this image in PDF format in addition to the default Artbrigade formats.
2) Chatterly advert picture. 1200px by 628px, RGB jpeg. This must comply with Chatterly’s restrictions on amount of text, which is no more than 20% of area taken up by text.(https://www.chatterly.example/ads/tools/text_overlay).
Because of these restrictions it is sufficient to include just the title and the author's name in this version.
3) Chatterly cover picture: 851px by 314px. RGB jpeg. It is sufficient to include just the title and the author's name in this version.
4) Web banner. 1000px by 300px. RGB jpeg. This version should include just the main image(s), no text.
Theatergoers
Entertainment

```html
<!DOCTYPE html>
<html lang="en">
<head>
<meta charset="utf-8">
<title>Lantern Field – Poster</title>
<link href="https://fonts.googleapis.com/css2?family=Cinzel:wght@400;700&family=Cormorant+Garamond:wght@500&family=Black+Ops+One&display=swap" rel="stylesheet">
<style>
  :root {
    --ink: #000000;
    --paper: #ffffff;
    --mist: #e9ece8;
    --leaf-light: #c9d9a0;
    --leaf: #6f9a3a;
    --moss: #2d4a22;
    --bark: #3a403c;
    --steel-hi: #f4f4f4;
    --steel-lo: #8a8d8f;
  }
  html, body {
    margin: 0;
    padding: 0;
    overflow: hidden;
    background: var(--ink);
  }
  .poster {
    position: relative;
    width: 849px;
    height: 1200px;
    overflow: hidden;
    background: var(--ink);
    color: var(--paper);
    font-family: "Cinzel", serif;
  }
  .hollow-art {
    position: absolute;
    inset: 0;
    background:
      radial-gradient(ellipse 210px 230px at 470px 640px, var(--mist) 0%, #d4dcc6 35%, var(--leaf-light) 55%, rgba(111,154,58,0.7) 72%, rgba(45,74,34,0) 100%),
      radial-gradient(ellipse 360px 420px at 450px 660px, var(--bark) 0%, #262a28 55%, rgba(0,0,0,0) 100%),
      var(--ink);
  }
  .presenter {
    position: absolute;
    top: 50px;
    right: 44px;
    display: flex;
    align-items: center;
    gap: 16px;
  }
  .presenter-name {
    font-family: "Cinzel", serif;
    font-weight: 700;
    font-size: 16px;
    line-height: 1.35;
    text-align: right;
    color: var(--paper);
  }
  .presenter-mark {
    width: 84px;
    height: 84px;
    border: 4px solid var(--paper);
    border-radius: 50%;
    box-sizing: border-box;
  }
  .tagline {
    position: absolute;
    top: 154px;
    left: 0;
    width: 849px;
    text-align: center;
    margin: 0;
    font-family: "Cormorant Garamond", serif;
    font-weight: 500;
    font-size: 23px;
    letter-spacing: 1.6px;
  }
  .title {
    position: absolute;
    top: 200px;
    left: 22px;
    width: 810px;
    height: 160px;
  }
  .byline {
    position: absolute;
    top: 362px;
    width: 849px;
    text-align: center;
    margin: 0;
    font-size: 36px;
    letter-spacing: 2px;
  }
  .director {
    position: absolute;
    top: 410px;
    width: 849px;
    text-align: center;
    margin: 0;
    font-size: 22px;
    letter-spacing: 2px;
  }
  .dates {
    position: absolute;
    top: 1066px;
    left: 20px;
    width: 440px;
    text-align: center;
    font-size: 31px;
    line-height: 38px;
    letter-spacing: 1px;
  }
  .venue {
    position: absolute;
    top: 1068px;
    left: 460px;
    width: 372px;
    text-align: center;
    font-size: 24px;
    line-height: 30px;
    letter-spacing: 2px;
  }
  .site {
    position: absolute;
    top: 1152px;
    font-family: "Cormorant Garamond", serif;
    font-weight: 500;
    font-size: 25px;
    letter-spacing: 2px;
  }
  .site-group { left: 37px; }
  .site-venue { right: 24px; }
</style>
</head>
<body>
<main class="poster">
  <div class="hollow-art" role="img" aria-label="Dark tree hollow opening onto sunlit green leaves, with the silhouettes of a couple holding a small child's hands between them"></div>

  <header class="presenter">
    <div class="presenter-name">Lakeshore Stage<br>Players Circle<br>presents</div>
    <div class="presenter-mark" aria-hidden="true"></div>
  </header>

  <p class="tagline">How do you keep it together when your whole world's fallen apart?</p>

  <svg class="title" viewBox="0 0 810 160" role="heading" aria-level="1" aria-label="Lantern Field">
    <defs>
      <linearGradient id="steel" x1="0" y1="0" x2="0" y2="1">
        <stop offset="0" stop-color="var(--steel-hi)"/>
        <stop offset="0.55" stop-color="#cfd1d2"/>
        <stop offset="1" stop-color="var(--steel-lo)"/>
      </linearGradient>
    </defs>
    <text x="405" y="128" text-anchor="middle" textLength="800" lengthAdjust="spacingAndGlyphs"
          font-family="'Black Ops One', sans-serif" font-size="118" fill="url(#steel)">LANTERN FIELD</text>
  </svg>

  <p class="byline">By Marcus Ellery-Pound</p>
  <p class="director">directed by Rob Feltwick</p>

  <div class="dates">1-5 March 2016<br>(Tue-Fri 20:00, Sat 19:00)</div>
  <div class="venue">Théâtre du Vieux-Moulin<br>Eaux-Vives, Geneva</div>

  <div class="site site-group">www.lspc.ch</div>
  <div class="site site-venue">www.scenelettres.ch</div>
</main>
</body>
</html>
```